Design a Label for a Line of Herbal Products

I am looking to hire a graphic designer for a long term project. I own a herbal shop and need new labels for my items. I am looking for labels with the color pink, must include photos of plants, text must be legible, must be modern.

I have attached documents from my business to provide as a guide for the type of look I am in search of.

Text: Seraphine Herbal Nest Tea
Subtext: Organic Loose herbs to support menstruation, strengthen the uterine wall and reduce menstrual flow.

Directions: Steep 1 tablespoon of herbal blend for 3-5 minutes. Allow to cool before drinking.
Solbrookwellnessarts.com

```html
<!DOCTYPE html>
<html lang="en">
<head>
<meta charset="UTF-8">
<title>Seraphine Herbal Nest Tea – Label</title>
<link href="https://fonts.googleapis.com/css2?family=Cinzel:wght@400&family=Parisienne&display=swap" rel="stylesheet">
<style>
  :root {
    --label-grey: #d9d9d9;
    --frame-green: #4f7f56;
    --title-green: #5b8c5f;
    --band-green: #7dab6d;
    --band-purple: #8a5ba8;
    --band-divider: #eef2ea;
    --leaf-dark: #1f4a26;
    --leaf-mid: #3c7440;
    --brand-pink: #d0448c;
    --web-pink: #f9cde2;
    --text-light: #ffffff;
  }
  * { margin: 0; padding: 0; box-sizing: border-box; }
  html, body { width: 1200px; height: 1057px; overflow: hidden; background: #ffffff; }
  .label {
    position: relative;
    width: 1200px;
    height: 1057px;
    background: var(--label-grey);
    overflow: hidden;
  }
  .leaf {
    position: absolute;
    background: radial-gradient(ellipse at 45% 40%, var(--leaf-mid) 0%, var(--leaf-dark) 75%);
    border-radius: 50% 50% 46% 54% / 55% 48% 52% 45%;
  }
  .leaf--top-left { left: -20px; top: -30px; width: 200px; height: 255px; transform: rotate(-18deg); }
  .leaf--top-center { left: 215px; top: -20px; width: 185px; height: 140px; transform: rotate(12deg); }
  .leaf--bottom-center { left: 812px; top: 548px; width: 186px; height: 120px; transform: rotate(-8deg); }
  .leaf--bottom-right { left: 1030px; top: 440px; width: 180px; height: 225px; transform: rotate(14deg); }

  .brand {
    position: absolute;
    right: 40px;
    top: 70px;
    display: flex;
    flex-direction: column;
    align-items: flex-end;
    gap: 10px;
    font-family: 'Cinzel', serif;
    color: var(--brand-pink);
    white-space: nowrap;
  }
  .brand__name {
    display: flex;
    align-items: center;
    gap: 12px;
    font-size: 28px;
  }
  .brand__dot {
    width: 22px; height: 22px;
    border-radius: 50%;
    background: var(--brand-pink);
  }
  .brand__web { font-size: 18px; letter-spacing: 0.5px; }

  .title-frame {
    position: absolute;
    left: 77px;
    top: 230px;
    width: 1046px;
    height: 316px;
    border: 3px solid var(--frame-green);
  }
  .title {
    position: absolute;
    left: 77px;
    top: 263px;
    width: 1046px;
    text-align: center;
    font-family: 'Cinzel', serif;
    font-weight: 400;
    font-size: 82px;
    line-height: 124px;
    color: var(--title-green);
    letter-spacing: 1px;
  }

  .band {
    position: absolute;
    left: 0;
    width: 1200px;
    padding-left: 40px;
    font-family: 'Parisienne', cursive;
    color: var(--text-light);
    white-space: nowrap;
  }
  .band--description {
    top: 657px;
    height: 180px;
    background: var(--band-green);
    padding-top: 14px;
    font-size: 54px;
    line-height: 76px;
  }
  .band--directions {
    top: 837px;
    height: 220px;
    background: var(--band-purple);
    padding-top: 28px;
    font-size: 47px;
    line-height: 70px;
    border-top: 3px solid var(--band-divider);
  }
  .web {
    position: absolute;
    right: 40px;
    bottom: 30px;
    font-family: 'Cinzel', serif;
    font-size: 22px;
    color: var(--web-pink);
    letter-spacing: 0.5px;
  }
</style>
</head>
<body>
  <main class="label">
    <div class="leaf leaf--top-left" role="img" aria-label="Monstera leaf illustration"></div>
    <div class="leaf leaf--top-center" role="img" aria-label="Monstera leaf illustration"></div>

    <div class="brand">
      <span class="brand__name"><span class="brand__dot"></span>Solbrook Yoga</span>
    </div>

    <div class="title-frame"></div>
    <h1 class="title">Seraphine Herbal<br>Nest Tea</h1>

    <div class="leaf leaf--bottom-center" role="img" aria-label="Monstera leaf illustration"></div>
    <div class="leaf leaf--bottom-right" role="img" aria-label="Monstera leaf illustration"></div>

    <p class="band band--description">Organic Loose herbs to support menstruation,<br>strengthen the uterine wall and reduce menstrual flow.</p>
    <div class="band band--directions">
      <p>Directions: Steep 1 tablespoon of herbal blend for 3-5 minutes.<br>Allow to cool before drinking.</p>
      <p class="web">Solbrookwellnessarts.com</p>
    </div>
  </main>
</body>
</html>
```